PowerPoint Template Design for Quarry Lending

Design a PowerPoint template for Quarry Lending, tailored for presentations to sophisticated mortgage servicing investors. The template should reflect a high level of professionalism, with a clean and modern aesthetic that resonates with an informed and discerning audience. The design must effectively integrate Quarry Lending's branding elements, ensuring a coherent visual narrative that reinforces our reputation for expertise and reliability in the mortgage servicing sector.

```html
<!DOCTYPE html>
<html lang="en">
<head>
<meta charset="utf-8">
<title>Quarry Lending – Presentation Template</title>
<link href="https://fonts.googleapis.com/css2?family=Montserrat:wght@400;500;600;700&family=Open+Sans:wght@400;600;700&display=swap" rel="stylesheet">
<style>
:root{
  --board:#ececec;
  --paper:#ffffff;
  --paper-soft:#f3f3f3;
  --teal:#36b0ae;
  --teal-light:#8fd3d1;
  --ink:#222429;
  --slate:#2b2e35;
  --grey:#c9c9c9;
  --grey-light:#dedede;
  --orange:#f0a030;
  --gold:#d9b24a;
}
*{box-sizing:border-box;margin:0;padding:0}
html,body{width:1200px;height:872px;overflow:hidden;background:var(--board)}
body{font-family:"Open Sans",Arial,sans-serif;color:var(--ink);position:relative}
.slide{position:absolute;width:245px;height:138px;background:var(--paper);overflow:hidden;box-shadow:5px 7px 9px rgba(0,0,0,.35)}
.slide.soft{background:var(--paper-soft)}
.abs{position:absolute}
.photo{position:absolute}
.dusk{background:linear-gradient(180deg,#3b4660 0%,#5a5a5e 38%,#6e5a3e 62%,#3f5a2e 100%)}
.villa{background:linear-gradient(180deg,#9fc3e6 0%,#eef0f0 40%,#d8d8d4 62%,#3aa7c9 78%,#4f7a3a 100%)}
.tower{background:linear-gradient(180deg,#b8cce0 0%,#e8e8e6 45%,#9a9c98 75%,#6f8a55 100%)}
.cottage{background:linear-gradient(180deg,#a9c6e2 0%,#f0efe9 45%,#b68a5a 70%,#6f8f4a 100%)}
.heading{font-family:"Montserrat",Arial,sans-serif;color:var(--teal);font-weight:500;font-size:10.5px;line-height:1.15}
.body{font-size:3.7px;line-height:1.45;color:var(--ink)}
.body.bold{font-weight:700}
.body.white{color:#fff}
.para{font-size:4.6px;line-height:1.4;color:var(--ink)}
.frame{position:absolute;border:.8px solid var(--teal)}
.bullet{position:absolute;display:flex;gap:3px}
.bullet::before{content:"";width:0;height:0;border-left:3px solid var(--teal);border-top:1.6px solid transparent;border-bottom:1.6px solid transparent;margin-top:1px;flex:none}
.year{position:absolute;font-family:"Montserrat",Arial,sans-serif;font-weight:700;font-size:5.5px;text-align:center;width:40px}
.year-box{position:absolute;width:36px;height:34px;display:flex;flex-direction:column;align-items:center;justify-content:center;color:#fff;font-family:"Montserrat",Arial,sans-serif;font-weight:700;font-size:5.5px}
.check-row{position:absolute;display:flex;align-items:center;gap:5px;width:112px}
.check-icon{flex:none;width:10px;height:10px}
.label-bar{position:absolute;height:8px;width:40px;background:var(--teal);color:#fff;font-size:4px;font-weight:700;text-align:center;line-height:8px}
.placeholder{position:absolute;background:var(--grey-light)}
</style>
</head>
<body>

<!-- Row 1 -->
<section class="slide" style="left:63px;top:110px">
  <div class="photo dusk" style="inset:0" role="img" aria-label="Modern house at dusk with lit windows"></div>
  <div class="abs" style="left:0;right:0;top:8px;text-align:center;font-family:'Montserrat',Arial,sans-serif;font-weight:600;font-size:6.5px;color:var(--gold)">Quarry Lending</div>
  <div class="abs" style="left:46px;top:46px;width:154px;height:34px;border:.8px solid #fff"></div>
  <div class="abs" style="left:46px;width:154px;top:52px;text-align:center;font-family:'Montserrat',Arial,sans-serif;color:#fff;font-size:10px;letter-spacing:4.5px">YOUR TITLE</div>
  <div class="abs" style="left:46px;width:154px;top:69px;text-align:center;font-family:'Montserrat',Arial,sans-serif;color:#fff;font-size:5px;letter-spacing:3px">HERE</div>
</section>

<section class="slide soft" style="left:343px;top:110px">
  <div class="heading abs" style="left:11px;top:28px">Lorem<br>Ipsum sit</div>
  <div class="bullet" style="left:11px;top:60px;width:78px"><p class="body bold">Lorem ipsum dolor sit amet, consectetuer adipiscing elit, sed diam nonummy nibh euismod tincidunt ut laoreet dolore</p></div>
  <div class="bullet" style="left:11px;top:87px;width:78px"><p class="body bold">Lorem ipsum dolor sit amet, consectetuer adipiscing elit, sed diam nonummy nibh euismod tincidunt ut laoreet</p></div>
  <div class="frame" style="left:94px;top:28px;width:134px;height:89px"></div>
  <div class="photo villa" style="left:107px;top:37px;width:98px;height:70px" role="img" aria-label="White modern villa with swimming pool"></div>
</section>

<section class="slide" style="left:623px;top:110px">
  <div class="photo villa" style="left:0;top:0;width:130px;height:138px" role="img" aria-label="White modern villa with swimming pool"></div>
  <div class="heading abs" style="right:12px;top:18px;text-align:right">Lorem<br>Ipsum sit</div>
  <p class="para abs" style="left:141px;top:55px;width:96px;font-size:4.3px">Lorem ipsum dolor sit amet, consectetur adipiscing elit, sed diam nvel eum iriure dolor in hendrerit in vulputate velit esse</p>
  <div class="abs" style="left:139px;top:104px;width:93px;height:22px;background:var(--teal);padding:3px 5px"><p class="body bold white" style="text-align:right">Lorem ipsum dolor sit amet, consectetuer adipiscing elit, sed diam nonummy nibh euismod</p></div>
</section>

<section class="slide" style="left:903px;top:110px">
  <div class="bullet" style="left:16px;top:14px;width:82px"><p class="body bold">Lorem ipsum dolor sit amet, consectetuer adipiscing elit, sed diam nonummy nibh euismod</p></div>
  <div class="bullet" style="left:16px;top:36px;width:82px"><p class="body bold">Lorem ipsum dolor sit amet, consectetuer adipiscing elit, sed diam nonummy nibh euismod</p></div>
  <div class="heading abs" style="left:16px;top:90px">Lorem<br>Ipsum sit</div>
  <div class="frame" style="left:108px;top:10px;width:94px;height:52px;border-color:var(--teal-light)"></div>
  <div class="photo tower" style="left:117px;top:16px;width:88px;height:47px" role="img" aria-label="White apartment building"></div>
  <div class="frame" style="left:158px;top:78px;width:76px;height:52px;border-color:var(--teal-light)"></div>
  <div class="photo cottage" style="left:152px;top:71px;width:74px;height:48px" role="img" aria-label="Family house with garage"></div>
</section>

<!-- Row 2 -->
<section class="slide soft" style="left:63px;top:277px">
  <div class="photo tower" style="left:83px;top:0;width:82px;height:138px" role="img" aria-label="Residential apartment buildings along a street"></div>
  <div class="abs" style="left:79px;top:0;width:1px;height:138px;background:#fff"></div>
  <div class="abs" style="left:168px;top:0;width:1px;height:138px;background:#fff"></div>
  <div class="year" style="left:18px;top:22px">1896<p class="body" style="font-weight:400;margin-top:2px">Lorem ipsum dolor sit amet, consectetuer adip elit</p></div>
  <div class="year-box" style="left:20px;top:57px;background:var(--teal)">1914<p class="body white" style="font-weight:400;margin-top:2px;text-align:center">Lorem ipsum dolor sit amet elit</p></div>
  <div class="year" style="left:18px;top:103px">1956<p class="body" style="font-weight:400;margin-top:2px">Lorem ipsum dolor sit amet, consectetuer adip elit</p></div>
  <div class="year" style="left:183px;top:22px">2003<p class="body" style="font-weight:400;margin-top:2px">Lorem ipsum dolor sit amet, consectetuer adip elit</p></div>
  <div class="year-box" style="left:185px;top:57px;background:var(--orange)">2011<p class="body white" style="font-weight:400;margin-top:2px;text-align:center">Lorem ipsum dolor sit amet elit</p></div>
  <div class="year" style="left:183px;top:103px">2018<p class="body" style="font-weight:400;margin-top:2px">Lorem ipsum dolor sit amet, consectetuer adip elit</p></div>
</section>

<section class="slide" style="left:343px;top:277px">
  <div class="heading abs" style="left:15px;top:11px">Lorem<br>Ipsum sit</div>
  <p class="para abs" style="left:15px;top:38px;width:100px;font-weight:600">Lorem ipsum dolor sit amet, consectetur adipiscing elit, sed diam nonummy nibh euismod</p>
  <svg class="abs" style="left:12px;top:80px" width="110" height="50" viewBox="0 0 110 50">
    <g font-family="Open Sans,Arial,sans-serif" font-size="3.2" fill="#222">
      <text x="0" y="6">150</text><text x="0" y="16">100</text><text x="0" y="26">50</text><text x="0" y="36">0</text>
      <text x="20" y="21">180</text><text x="30" y="27">60</text><text x="42" y="17">270</text><text x="54" y="21">210</text><text x="66" y="9">450</text><text x="80" y="23">100</text>
    </g>
    <path d="M10 38 C18 38 20 24 26 24 C32 24 34 32 38 32 C42 32 44 20 48 20 C54 20 56 27 60 27 C66 27 66 10 72 10 C78 10 80 30 88 32 L94 34 L94 38 Z" fill="var(--teal)"/>
    <line x1="8" y1="38" x2="106" y2="38" stroke="#222" stroke-width=".5"/>
  </svg>
  <svg class="abs" style="left:110px;top:0" width="135" height="138" viewBox="0 0 135 138" role="img" aria-label="Living room interior in a diamond frame">
    <polygon points="72,8 132,64 72,120 12,64" fill="none" stroke="var(--teal)" stroke-width=".8" transform="translate(8,12)"/>
    <defs><linearGradient id="room" x1="0" y1="0" x2="1" y2="1"><stop offset="0" stop-color="#efe8dc"/><stop offset=".5" stop-color="#c6b49a"/><stop offset="1" stop-color="#8d7c66"/></linearGradient></defs>
    <polygon points="70,0 128,56 70,112 12,56" fill="url(#room)"/>
  </svg>
</section>

<section class="slide" style="left:623px;top:277px">
  <div class="photo cottage" style="left:0;top:0;width:84px;height:138px" role="img" aria-label="Modern family house with wood panels"></div>
  <div class="abs" style="left:74px;top:8px;width:14px;height:122px;border:.8px solid var(--teal);border-left:none"></div>
  <div class="heading abs" style="left:122px;top:11px">Lorem<br>Ipsum sit</div>
  <p class="para abs" style="left:122px;top:40px;width:112px;font-size:3.9px">Lorem ipsum dolor sit amet, consectetuer adipiscing elit, sed diam nonummy nibh euismod tincidunt ut laoreet dolore magna aliquam erat volutpat. Ut wisi enim ad minim veniam, quis nostrud exerci tation.</p>
  <svg class="abs" style="left:120px;top:95px" width="100" height="30" viewBox="0 0 100 30">
    <g stroke="var(--teal)" stroke-width="1.4"><line x1="2" y1="4" x2="60" y2="4"/><line x1="2" y1="11" x2="80" y2="11"/><line x1="2" y1="18" x2="54" y2="18"/><line x1="2" y1="25" x2="44" y2="25"/></g>
    <g fill="var(--teal)"><circle cx="60" cy="4" r="1.4"/><circle cx="80" cy="11" r="1.4"/><circle cx="54" cy="18" r="1.4"/><circle cx="44" cy="25" r="1.4"/></g>
    <g font-family="Open Sans,Arial,sans-serif" font-size="3.6" fill="#222"><text x="64" y="5.5">28</text><text x="84" y="12.5">25</text><text x="58" y="19.5">20</text><text x="48" y="26.5">20</text></g>
  </svg>
</section>

<section class="slide" style="left:903px;top:277px">
  <div class="heading abs" style="left:0;right:0;top:6px;text-align:center;font-size:10px">Lorem ipsum sit</div>
  <svg class="abs" style="left:0;top:26px" width="245" height="20" viewBox="0 0 245 20">
    <g fill="none" stroke="var(--teal)" stroke-width=".9">
      <g transform="translate(39,2)"><rect x="0" y="3" width="14" height="10"/><path d="M-1 3 L7 -1 L15 3"/><rect x="5" y="7" width="4" height="6"/></g>
      <g transform="translate(117,2)"><rect x="0" y="3" width="14" height="10"/><path d="M-1 3 L7 -1 L15 3"/><rect x="5" y="7" width="4" height="6"/></g>
      <g transform="translate(195,2)"><rect x="0" y="3" width="14" height="10"/><path d="M-1 3 L7 -1 L15 3"/><rect x="5" y="7" width="4" height="6"/></g>
    </g>
  </svg>
  <div class="abs" style="left:22px;top:44px;width:48px;text-align:center"><p class="body bold">LOREM IPSUM DOLOR</p><p class="body">Lorem ipsum dolor sit amet, consectetuer adipiscing elit sed</p></div>
  <div class="abs" style="left:100px;top:44px;width:48px;text-align:center"><p class="body bold">LOREM IPSUM DOLOR</p><p class="body">Lorem ipsum dolor sit amet, consectetuer adipiscing elit sed</p></div>
  <div class="abs" style="left:178px;top:44px;width:48px;text-align:center"><p class="body bold">LOREM IPSUM DOLOR</p><p class="body">Lorem ipsum dolor sit amet, consectetuer adipiscing elit sed</p></div>
  <div class="photo dusk" style="left:0;top:80px;width:245px;height:58px" role="img" aria-label="Large house with warm lights at dusk"></div>
</section>

<!-- Row 3 -->
<section class="slide" style="left:63px;top:448px">
  <svg class="abs" style="inset:0" width="245" height="138" viewBox="0 0 245 138">
    <polygon points="0,0 245,0 245,138 172,138 0,64" fill="var(--teal)"/>
    <line x1="68" y1="0" x2="245" y2="104" stroke="#fff" stroke-width="1.4"/>
    <line x1="0" y1="68" x2="168" y2="138" stroke="var(--teal)" stroke-width=".7"/>
    <line x1="0" y1="76" x2="150" y2="138" stroke="#fff" stroke-width=".7"/>
  </svg>
  <div class="heading abs" style="left:22px;top:16px;color:#fff">Lorem<br>Ipsum sit</div>
  <p class="body bold white abs" style="left:76px;top:55px;width:70px">Lorem ipsum dolor sit amet, consectetuer adipiscing elit, sed diam nonummy nibh euismod</p>
  <p class="body bold white abs" style="left:112px;top:75px;width:70px">Lorem ipsum dolor sit amet, consectetuer adipiscing elit, sed diam nonummy nibh euismod</p>
  <p class="body bold white abs" style="left:142px;top:98px;width:70px">Lorem ipsum dolor sit amet, consectetuer adipiscing elit, sed diam nonummy nibh euismod</p>
</section>

<section class="slide" style="left:343px;top:448px">
  <div class="heading abs" style="left:0;right:0;top:8px;text-align:center;font-size:10.5px;letter-spacing:.5px">Chart infographic</div>
  <p class="body abs" style="left:0;right:0;top:22px;text-align:center;color:#888">Type the subtitle of your great here</p>
  <svg class="abs" style="left:24px;top:32px" width="200" height="80" viewBox="0 0 200 80">
    <g stroke="#e2e2e2" stroke-width=".4"><line x1="8" y1="8" x2="196" y2="8"/><line x1="8" y1="22" x2="196" y2="22"/><line x1="8" y1="36" x2="196" y2="36"/><line x1="8" y1="50" x2="196" y2="50"/><line x1="8" y1="64" x2="196" y2="64"/></g>
    <g font-family="Open Sans,Arial,sans-serif" font-size="3" fill="#666"><text x="0" y="9">100</text><text x="1" y="23">80</text><text x="1" y="37">60</text><text x="1" y="51">40</text><text x="1" y="65">20</text><text x="3" y="77">0</text></g>
    <g fill="var(--teal)"><rect x="16" y="8" width="7" height="68"/><rect x="46" y="14" width="7" height="62"/><rect x="76" y="40" width="7" height="36"/><rect x="106" y="8" width="7" height="68"/><rect x="136" y="8" width="7" height="68"/><rect x="166" y="42" width="7" height="34"/></g>
    <g fill="var(--grey)"><rect x="25" y="14" width="7" height="62"/><rect x="55" y="10" width="7" height="66"/><rect x="85" y="8" width="7" height="68"/><rect x="115" y="34" width="7" height="42"/><rect x="145" y="14" width="7" height="62"/><rect x="175" y="8" width="7" height="68"/></g>
    <line x1="8" y1="76" x2="196" y2="76" stroke="#888" stroke-width=".4"/>
  </svg>
  <p class="body abs" style="left:22px;right:22px;top:113px;text-align:center;color:#555;font-size:3.2px">Lorem ipsum dolor sit amet, consectetuer adipiscing elit, sed diam nonummy nibh euismod tincidunt ut laoreet dolore magna aliquam erat volutpat. Ut wisi enim ad minim veniam, quis nostrud exerci tation ullamcorper suscipit lobortis nisl ut aliquip ex ea commodo consequat, vel illum dolore.</p>
</section>

<section class="slide" style="left:623px;top:448px">
  <div class="heading abs" style="left:22px;top:16px">Lorem<br>Ipsum sit</div>
  <p class="para abs" style="left:22px;top:44px;width:72px;font-size:4.1px">Lorem ipsum dolor sit amet, cons ectetuer adipiscing elit, sed diam nonummy nibh euismod tincidunt ut laoreet dolore magna aliquam erat volutpat. Ut wisi enim ad minim veniam, quis nostrud exerci tation ullamcorper suscipit lobortis nisl ut aliquip ex ea commodo consequat. Duis autem vel eum iriure dolor.</p>
  <svg class="abs" style="left:100px;top:0" width="145" height="138" viewBox="0 0 145 138" role="img" aria-label="Bright living room with television wall">
    <defs><linearGradient id="lounge" x1="0" y1="0" x2="1" y2="1"><stop offset="0" stop-color="#efece6"/><stop offset=".55" stop-color="#cfc6ba"/><stop offset="1" stop-color="#9a8f82"/></linearGradient></defs>
    <polygon points="10,0 145,0 145,138 0,138" fill="url(#lounge)"/>
    <polygon points="48,0 52,0 36,138 32,138" fill="#fff"/>
    <polygon points="64,0 68,0 52,138 48,138" fill="#fff"/>
  </svg>
</section>

<section class="slide checklist" style="left:903px;top:448px">
  <svg class="abs" style="inset:0" width="245" height="138" viewBox="0 0 245 138">
    <polygon points="148,0 245,0 200,58" fill="var(--teal)"/>
    <polygon points="0,138 60,86 110,138" fill="var(--teal)"/>
  </svg>
  <div class="heading abs" style="left:16px;top:7px">Lorem<br>Ipsum sit</div>
  <div class="check-row" style="left:38px;top:32px">
    <svg class="check-icon" viewBox="0 0 10 10"><circle cx="5" cy="5" r="4.4" fill="none" stroke="var(--teal)" stroke-width=".8"/><path d="M2.9 5 l1.6 1.6 l2.8 -3.2" fill="none" stroke="var(--teal)" stroke-width=".8"/></svg>
    <p class="body">Lorem ipsum dolor sit amet, consectetuer adipiscing elit, sed diam nonummy tempor incididunt.</p>
  </div>
  <div class="check-row" style="left:66px;top:55px">
    <svg class="check-icon" viewBox="0 0 10 10"><circle cx="5" cy="5" r="4.4" fill="none" stroke="var(--teal)" stroke-width=".8"/><path d="M2.9 5 l1.6 1.6 l2.8 -3.2" fill="none" stroke="var(--teal)" stroke-width=".8"/></svg>
    <p class="body">Lorem ipsum dolor sit amet, consectetuer adipiscing elit, sed diam nonummy tempor incididunt.</p>
  </div>
  <div class="check-row" style="left:94px;top:78px">
    <svg class="check-icon" viewBox="0 0 10 10"><circle cx="5" cy="5" r="4.4" fill="none" stroke="var(--teal)" stroke-width=".8"/><path d="M2.9 5 l1.6 1.6 l2.8 -3.2" fill="none" stroke="var(--teal)" stroke-width=".8"/></svg>
    <p class="body">Lorem ipsum dolor sit amet, consectetuer adipiscing elit, sed diam nonummy tempor incididunt.</p>
  </div>
  <div class="check-row" style="left:120px;top:101px">
    <svg class="check-icon" viewBox="0 0 10 10"><circle cx="5" cy="5" r="4.4" fill="none" stroke="var(--teal)" stroke-width=".8"/><path d="M2.9 5 l1.6 1.6 l2.8 -3.2" fill="none" stroke="var(--teal)" stroke-width=".8"/></svg>
    <p class="body">Lorem ipsum dolor sit amet, consectetuer adipiscing elit, sed diam nonummy tempor incididunt.</p>
  </div>
</section>

<!-- Row 4 -->
<section class="slide" style="left:63px;top:615px">
  <div class="heading abs" style="left:0;right:0;top:9px;text-align:center;font-size:10px">Lorem Ipsum sit</div>
  <svg class="abs" style="left:0;top:30px" width="245" height="60" viewBox="0 0 245 60">
    <g transform="translate(43,0)"><polygon points="0,4 24,28 0,52 -24,28" fill="var(--grey-light)"/><path d="M-22 20 L0 -2 L22 20" fill="none" stroke="var(--teal)" stroke-width="2.4"/></g>
    <g transform="translate(122,0)"><polygon points="0,4 24,28 0,52 -24,28" fill="var(--grey-light)"/><path d="M-22 20 L0 -2 L22 20" fill="none" stroke="var(--teal)" stroke-width="2.4"/></g>
    <g transform="translate(201,0)"><polygon points="0,4 24,28 0,52 -24,28" fill="var(--grey-light)"/><path d="M-22 20 L0 -2 L22 20" fill="none" stroke="var(--teal)" stroke-width="2.4"/></g>
  </svg>
  <div class="abs" style="left:18px;top:96px;width:50px;text-align:center"><p class="body bold">YOUR TITLE</p><p class="body">Lorem ipsum dolor sit amet, consectetuer adipiscing elit, sed diam tincidunt.</p></div>
  <div class="abs" style="left:97px;top:96px;width:50px;text-align:center"><p class="body bold">YOUR TITLE</p><p class="body">Lorem ipsum dolor sit amet, consectetuer adipiscing elit, sed diam tincidunt.</p></div>
  <div class="abs" style="left:176px;top:96px;width:50px;text-align:center"><p class="body bold">YOUR TITLE</p><p class="body">Lorem ipsum dolor sit amet, consectetuer adipiscing elit, sed diam tincidunt.</p></div>
</section>

<section class="slide" style="left:343px;top:615px">
  <div class="heading abs" style="left:0;right:0;top:4px;text-align:center;font-size:10px">Lorem Ipsum sit</div>
  <div class="placeholder" style="left:26px;top:28px;width:40px;height:40px"></div>
  <div class="placeholder" style="left:102px;top:28px;width:40px;height:40px"></div>
  <div class="placeholder" style="left:170px;top:28px;width:40px;height:40px"></div>
  <div class="label-bar" style="left:26px;top:71px">YOUR TITLE</div>
  <div class="label-bar" style="left:102px;top:71px">YOUR TITLE</div>
  <div class="label-bar" style="left:170px;top:71px">YOUR TITLE</div>
  <p class="body bold abs" style="left:24px;top:83px;width:46px;text-align:center">Diam nonummy nibh euismod tincidunt ut laoreet dolore magna aliquam erat</p>
  <p class="body bold abs" style="left:100px;top:83px;width:46px;text-align:center">Diam nonummy nibh euismod tincidunt ut laoreet dolore magna aliquam erat</p>
  <p class="body bold abs" style="left:168px;top:83px;width:46px;text-align:center">Diam nonummy nibh euismod tincidunt ut laoreet dolore magna aliquam erat</p>
</section>

<section class="slide" style="left:623px;top:615px;background:var(--slate)">
  <div class="photo villa" style="left:0;top:0;width:128px;height:78px" role="img" aria-label="White modern villa with swimming pool"></div>
  <svg class="abs" style="inset:0" width="245" height="138" viewBox="0 0 245 138">
    <polygon points="0,84 140,84 124,138 0,138" fill="var(--teal)"/>
  </svg>
  <div class="photo cottage" style="left:138px;top:84px;width:107px;height:54px;clip-path:polygon(16px 0,100% 0,100% 100%,0 100%)" role="img" aria-label="Family house with garage"></div>
  <div class="heading abs" style="left:14px;top:94px;color:#fff">Lorem<br>Ipsum sit</div>
  <p class="body bold white abs" style="left:134px;top:12px;width:48px">Diam nonummy nibh euismod tincidunt ut laoreet dolore magna aliquam erat</p>
  <p class="body bold white abs" style="left:188px;top:12px;width:48px">Diam nonummy nibh euismod tincidunt ut laoreet dolore magna aliquam erat</p>
  <p class="body bold white abs" style="left:134px;top:44px;width:48px">Diam nonummy nibh euismod tincidunt ut laoreet dolore magna aliquam erat</p>
  <p class="body bold white abs" style="left:188px;top:44px;width:48px">Diam nonummy nibh euismod tincidunt ut laoreet dolore magna aliquam erat</p>
</section>

<section class="slide" style="left:903px;top:615px">
  <div class="photo dusk" style="inset:0" role="img" aria-label="Two-storey house with warm lights at dusk"></div>
  <div class="abs" style="left:0;right:0;top:32px;text-align:center;font-family:'Montserrat',Arial,sans-serif;color:#fff;font-size:16px;font-weight:500;letter-spacing:.5px">THANK YOU!</div>
  <div class="abs" style="left:30px;top:72px;width:52px;text-align:center;color:#fff"><p style="font-size:6px;font-weight:600">Location</p><p class="body bold white">Lorem ipsum dolor sit amet, consectetuer.</p></div>
  <div class="abs" style="left:96px;top:72px;width:54px;text-align:center;color:#fff"><p style="font-size:6px;font-weight:600">Phone Number</p><p class="body bold white">Lorem ipsum dolor sit amet, consectetuer.</p></div>
  <div class="abs" style="left:166px;top:72px;width:52px;text-align:center;color:#fff"><p style="font-size:6px;font-weight:600">Email</p><p class="body bold white">Lorem ipsum dolor sit amet, consectetuer.</p></div>
</section>

</body>
</html>
```